Website redesign and new logo

Hi we feel that the colours, layout and style along with the logo which is only text at the moment is poor. It seems to lack a quality and luxurious feel and we are about selling high end curtains. The text logo is hard to read as well in my opinion. We are looking for a overall revamp and an new logo. We want to maintain the main parts of the home page but happy to consider any ideas that will improve web traffic. It does not really reflect our achievements either of having curtains recently featured on Horizon 7 tv.
The website in question is www.lunaviewinteriors.co.uk

```html
<!DOCTYPE html>
<html lang="en">
<head>
<meta charset="utf-8">
<title>Lunaview Interiors</title>
<link rel="stylesheet" href="https://fonts.googleapis.com/css2?family=Cinzel:wght@400;600&family=PT+Sans:ital,wght@0,400;0,700;1,400&display=swap">
<style>
:root{
  --teal:#0f8a8f;
  --teal-dark:#0a6a6e;
  --teal-light:#1fa3a6;
  --orange:#e29c00;
  --orange-light:#f2b31a;
  --ink:#222;
  --text:#6f6f6f;
  --muted:#8a8a8a;
  --pattern:#ececec;
  --footer-top:#d8ecec;
  --footer-bottom:#b9dcdd;
  --white:#fff;
}
*{box-sizing:border-box;margin:0;padding:0}
html,body{width:753px;height:1200px;overflow:hidden}
body{position:relative;background:var(--white);font-family:"PT Sans",sans-serif;color:var(--text)}
.abs{position:absolute}
.top-strip{left:0;top:0;width:753px;height:4px;background:#dcefef}
.brand{left:0;top:28px;width:753px;text-align:center;font-family:"Cinzel",serif;font-weight:600;font-size:27px;color:var(--teal);letter-spacing:1px}
.brand small{display:block;font-size:10px;letter-spacing:5px;margin-top:3px;font-weight:400}
.nav{left:0;top:83px;width:753px;height:35px;background:linear-gradient(#20a1a5,#0b7a7e);display:flex;align-items:center;justify-content:center;gap:0}
.nav a{color:var(--white);text-decoration:none;font-size:10px;letter-spacing:.2px;padding:0 11px;position:relative;line-height:35px}
.nav a+a::before{content:"";position:absolute;left:-2px;top:0;width:1px;height:35px;background:rgba(255,255,255,.35);transform:skewX(-25deg)}
.hero{left:0;top:118px;width:753px;height:276px;background:linear-gradient(100deg,#d9a35e 0%,#e9cfa0 30%,#f1ece2 55%,#d7b27a 75%,#5f9a45 100%)}
.hero-sofa{left:120px;top:210px;width:560px;height:184px;background:linear-gradient(#f4f2ee,#dedad3);border-radius:20px 20px 0 0;opacity:.85}
.tips{left:477px;top:166px;width:197px;height:202px;background:linear-gradient(#eaf6f6,#ffffff);border:2px solid var(--teal);border-top:none;border-radius:0 0 40% 40%/0 0 10px 10px}
.tips-valance{left:477px;top:166px;width:197px;height:18px;background:linear-gradient(var(--teal-light),var(--teal));border-radius:0 0 50% 50%/0 0 100% 100%}
.tips h2{position:absolute;left:0;top:35px;width:100%;text-align:center;font-family:"Cinzel",serif;font-weight:400;font-size:14px;color:var(--teal)}
.field{position:absolute;left:25px;width:143px;height:17px;border:1px solid #ccc;background:#fff;font-size:7.5px;line-height:15px;padding-left:10px;color:#666}
.submit{position:absolute;left:26px;top:128px;width:141px;height:20px;background:linear-gradient(var(--orange-light),var(--orange));color:#fff;font-size:9px;text-align:center;line-height:20px;border-radius:2px}
.tips p{position:absolute;left:20px;top:155px;width:155px;text-align:center;font-size:7.5px;line-height:11px;color:var(--teal)}
.dots{left:352px;top:372px;display:flex;gap:3px}
.dots i{display:block;width:10px;height:10px;border-radius:50%;background:#f4f0e8}
.dots i:first-child{background:var(--teal)}
.welcome{left:0;top:420px;width:753px;text-align:center}
.welcome h1{font-family:"Cinzel",serif;font-weight:400;font-size:22px;color:var(--ink);letter-spacing:.5px}
.welcome .lead{font-size:8.5px;color:#444;margin-top:6px}
.welcome .body{width:530px;margin:8px auto 0;font-size:8.3px;line-height:13.5px;color:var(--muted)}
.btn{display:block;background:linear-gradient(var(--teal-light),var(--teal-dark));color:#fff;font-size:8px;text-align:center;text-decoration:none}
.welcome .btn{left:327px;top:518px;width:80px;height:22px;line-height:22px}
.band{left:0;top:560px;width:753px;height:266px;background:var(--pattern)}
.card{top:592px;width:184px;height:193px;background:#fff;box-shadow:0 1px 4px rgba(0,0,0,.18)}
.card .photo{height:80px}
.card h3{font-family:"Cinzel",serif;font-weight:400;font-size:14px;color:var(--teal);margin:12px 0 0 16px;line-height:15px}
.card h3 span{display:block;font-size:10.5px;letter-spacing:.5px}
.card p{margin:6px 16px 0;font-size:7px;line-height:12px;color:var(--muted)}
.card .bar{position:absolute;left:0;bottom:0;width:100%;height:23px;background:var(--orange);color:#fff;font-size:7px;line-height:23px;padding-left:16px}
.card .bar::after{content:"";display:inline-block;margin-left:4px;border-left:4px solid #fff;border-top:3px solid transparent;border-bottom:3px solid transparent}
.quote-card h3{margin-top:16px;font-size:15px}
.quote-card h3 span{font-size:11px}
.avatar{position:absolute;left:17px;top:54px;width:48px;height:46px;background:linear-gradient(#d9c9b8,#8b7968)}
.quote{position:absolute;left:72px;top:52px;width:100px;font-size:7px;line-height:12px;font-style:italic;color:var(--muted)}
.quote-rest{position:absolute;left:17px;top:103px;width:160px;font-size:7px;line-height:12px;font-style:italic;color:var(--muted)}
.author{position:absolute;left:17px;top:135px;font-size:8px;color:#333}
.section-title{font-family:"Cinzel",serif;font-weight:400;font-size:15.5px;color:#333;letter-spacing:.5px}
.areas-title{left:68px;top:861px}
.areas-text{left:68px;top:887px;width:345px;font-size:8.3px;line-height:13.5px;color:var(--muted)}
.areas-list{list-style:none;font-size:8.5px;color:#444}
.areas-list li{height:19.5px;padding-left:13px;position:relative}
.areas-list li::before{content:"";position:absolute;left:1px;top:3px;width:6px;height:6px;background:#aac7c7;transform:rotate(45deg)}
.list-a{left:68px;top:942px}
.list-b{left:218px;top:942px}
.areas-btn{left:69px;top:1014px;width:77px;height:22px;line-height:22px;border-radius:2px}
.meet-title{left:444px;top:861px}
.video{left:445px;top:886px;width:239px;height:144px;border:1px solid #ddd;background:#fff;padding:5px;box-shadow:0 1px 3px rgba(0,0,0,.1)}
.video .photo{width:100%;height:100%;background:linear-gradient(90deg,#c4ad8a,#e8dcc5 35%,#f3efe6 55%,#d8c4a2 80%,#bca27a)}
.footer{left:0;top:1086px;width:753px;height:114px;background:linear-gradient(var(--footer-top),var(--footer-bottom))}
.foot-links{left:65px;top:1108px;font-size:8.5px;color:#2f4a4b}
.foot-links span{margin:0 3px;color:#555}
.copy{left:65px;top:1129px;font-size:7.5px;color:#4a6263}
.social{left:65px;top:1147px;display:flex;gap:3px}
.social i{display:block;width:18px;height:18px;border-radius:50%;background:var(--teal-dark)}
.contact{left:583px;top:1108px;font-size:8px;line-height:13.5px;color:#2f4a4b}
.contact strong{font-weight:400;font-size:9.5px}
.contact .phone{font-size:10.5px}
</style>
</head>
<body>
<div class="abs top-strip"></div>
<div class="abs brand">Lunaview<small>Interiors</small></div>

<nav class="abs nav">
  <a>HOME</a><a>ABOUT US</a><a>NEWS</a><a>FABRICS</a><a>SCATTER CUSHIONS &amp; BED THROWS</a><a>GALLERY</a><a>TESTIMONIALS</a><a>CONTACT US</a>
</nav>

<div class="abs hero" role="img" aria-label="Living room with white sofa, green cushions and green curtains"></div>
<div class="abs tips">
  <h2>FREE CURTAINS TIPS</h2>
  <div class="field" style="top:58px">Name</div>
  <div class="field" style="top:81px">Phone no.</div>
  <div class="field" style="top:104px">Email address</div>
  <div class="submit">SUBMIT NOW</div>
  <p>Aliquam vehicula mi at mauris Maecenas placerat nisl at consequat rhoncu</p>
</div>
<div class="abs tips-valance"></div>
<div class="abs dots"><i></i><i></i><i></i><i></i></div>

<section class="abs welcome">
  <h1>Welcome to Lunaview Interiors</h1>
  <p class="lead">Lorem ipsum dolor sit amet, consectetuer adipiscing elit. Nam cursus. Morbi ut mi. Nullam enim leo, egestas id, condimentum</p>
  <p class="body">Duis tincidunt lectus quis dui viverra vestibulum. Suspendisse vulputate aliquam dui. Nulla elementum dui ut augue. Aliquam vehicula mi at mauris. Maecenas placerat, nisl at consequat rhoncus, sem nunc gravida justo, quis eleifend arcu velit quis lacus. Morbi magna magna, tincidunt a, mattis non, imperdiet vitae, tellus. Sed odio est, auctor ac, sollicitudin in, consequat vitae, orci.</p>
</section>
<a class="abs btn welcome-btn" style="left:327px;top:518px;width:80px;height:22px;line-height:22px">LEARN MORE</a>

<div class="abs band" role="img" aria-label="Soft grey damask wallpaper pattern"></div>

<article class="abs card" style="left:78px">
  <div class="photo" role="img" aria-label="Gold draped curtains with swag valance" style="background:linear-gradient(90deg,#b88a45,#f0dcae 50%,#b88a45)"></div>
  <h3>Curtain Fabric<span>TYPES INCLUDE</span></h3>
  <p>Mauris vel lacus vitae felis vestibulum volutpat. Etiam est nunc, venenatis in, tristique eu, imperdiet ac nisl Cum sociis</p>
  <div class="bar">READING BY GUIDE</div>
</article>

<article class="abs card" style="left:282px">
  <div class="photo" role="img" aria-label="Cream curtains with red floral print" style="background:linear-gradient(90deg,#efe6dc,#d9a0a0 40%,#f4eee8 70%,#cfc7bd)"></div>
  <h3>Our Latest Curtain<span>AND FABRIC NEWS</span></h3>
  <p>Mauris vel lacus vitae felis vestibulum volutpat. Etiam est nunc, venenatis in, tristique eu, imperdiet ac nisl Cum sociis</p>
  <div class="bar">READING BY GUIDE</div>
</article>

<article class="abs card quote-card" style="left:486px">
  <h3>Our Customers<span>LOVE US</span></h3>
  <div class="avatar" role="img" aria-label="Customer portrait"></div>
  <p class="quote">Mauris vel lacus vitae felis vestibulum volutpat. Etiam est nunc, venenatis tristique eu imperdiet ac nisl sociis</p>
  <p class="quote-rest">Mauris vel lacus vitae felis vestibulum volutpat. Etiam est nunc, venenatis tristique</p>
  <p class="author">By Author Name</p>
  <div class="bar">VIEW ALL</div>
</article>

<h2 class="abs section-title areas-title">The Areas We Cover Include</h2>
<p class="abs areas-text">Duis tincidunt lectus quis dui viverra vestibulum. Suspendisse vulputate aliquam dui. Nulla elementum dui ut augue. Aliquam vehicula mi at mauris. Maecenas placerat, nisl at consequat rhoncus, sem nunc gravida justo, quis eleifend arcu velit quis lacus.</p>
<ul class="abs areas-list list-a">
  <li>Curtains Berkshire</li><li>Curtains Buckinghamshire</li><li>Curtains Oxfordshire</li>
</ul>
<ul class="abs areas-list list-b">
  <li>Curtains Winchester</li><li>Curtains Guildford</li><li>Curtains Oxford</li>
</ul>
<a class="abs btn areas-btn">READ MORE</a>

<h2 class="abs section-title meet-title">Meet Integrity Designer</h2>
<div class="abs video">
  <div class="photo" role="img" aria-label="Video still of beige curtains framing a child's room window"></div>
  <svg class="abs" style="left:105px;top:58px" width="24" height="24" viewBox="0 0 24 24" aria-hidden="true">
    <circle cx="12" cy="12" r="11" fill="#1c1c1c"/>
    <path d="M9.5 7.5 L16.5 12 L9.5 16.5 Z" fill="#fff"/>
  </svg>
</div>

<footer class="abs footer"></footer>
<div class="abs foot-links">HOME<span>|</span>ABOUT US<span>|</span>NEWS<span>|</span>FABRICS<span>|</span>SCATTER CUSHIONS &amp; BED THROWS<span>|</span>GALLERY<span>|</span>TESTIMONIALS<span>|</span>CONTACT US</div>
<div class="abs copy">Copyright © 2013 Company Name.&nbsp; All right reserved</div>
<div class="abs social"><i></i><i></i><i></i></div>
<address class="abs contact" style="font-style:normal">
  <strong>Lunaview Interiors</strong><br>
  14 Mill Lane,<br>
  Windsor, Berkshire, SL4 2QX<br>
  <span class="phone">0333 555 0192</span>
</address>
</body>
</html>
```